Business Card Design for New Game Studio

We need a business card design. We are a new company developing innovative mobile and platform games.

I would like to see very innovative design thats brings out the company's goal and direction.

My Company's goal and direction is to "Evolve the way of gaming, Bring fun and entertainment to all gamers"

Please do use our company logo which I have attached to be included in the design.

Please put in details for name, title, contacts etc ... be creative !!!
Updates

Reason: Company logo redesign. Awaiting it. Thanks

Hi all Please do wait for my updated company logo. Thanks

Reason: Still waiting on new company logo. Thanks all

Hi All Designers .... Sorry for the long wait... Please see the new file for my new company logo uploaded. Waiting to see all your creative design. Cheers

Hi All .... Please do not just mass send a whole bunch of similar designs .... Would like to see quality instead of quantity Cheers

Industry/Entity Type

Entertainment

```html
<!DOCTYPE html>
<html lang="en">
<head>
<meta charset="utf-8">
<title>Verdant Realty — Business Card</title>
<link rel="stylesheet" href="https://fonts.googleapis.com/css2?family=Cabin:wght@400&family=Roboto+Condensed:wght@700&display=swap">
<style>
  :root {
    --backdrop: #c0c1c3;
    --paper: #ffffff;
    --lime: #d4dc22;
    --slate: #878787;
    --ink: #111111;
    --muted: #7a7a7a;
  }
  * { margin: 0; padding: 0; box-sizing: border-box; }
  html, body { width: 1200px; height: 1200px; overflow: hidden; }
  body { background: var(--backdrop); position: relative; font-family: "Cabin", sans-serif; }

  .card { position: absolute; left: 227px; width: 754px; height: 450px; overflow: hidden; }
  .card--front { top: 138px; background: var(--paper); }
  .card--back { top: 619px; background: var(--lime); }

  .brand { position: absolute; left: 0; right: 0; display: flex; flex-direction: column; align-items: center; }
  .brand__square { display: block; }
  .brand__name { font-family: "Roboto Condensed", sans-serif; font-weight: 700; letter-spacing: 0.5px; white-space: nowrap; }

  .card--front .brand { top: 40px; }
  .card--front .brand__square { width: 62px; height: 62px; background: var(--lime); }
  .card--front .brand__name { margin-top: 70px; font-size: 26px; color: var(--lime); }

  .card--back .brand { top: 98px; }
  .card--back .brand__square { width: 86px; height: 86px; background: var(--paper); }
  .card--back .brand__name { margin-top: 112px; font-size: 38px; color: var(--paper); }

  .contact { position: absolute; left: 36px; top: 253px; list-style: none; color: var(--muted); font-size: 17px; line-height: 22px; }
  .contact__item { display: flex; align-items: flex-start; margin-bottom: 5px; }
  .contact__icon { width: 20px; height: 20px; margin-right: 10px; margin-top: 1px; fill: var(--muted); flex: none; }

  .person { position: absolute; right: 56px; top: 257px; text-align: right; font-family: "Roboto Condensed", sans-serif; font-weight: 700; }
  .person__name { font-size: 23px; color: var(--ink); line-height: 28px; letter-spacing: 0.3px; }
  .person__title { font-size: 19px; color: var(--lime); line-height: 22px; }

  .card__waves { position: absolute; left: 0; top: 0; width: 754px; height: 450px; }
</style>
</head>
<body>
  <section class="card card--front">
    <div class="brand">
      <span class="brand__square"></span>
      <span class="brand__name">Verdant Realty</span>
    </div>

    <ul class="contact">
      <li class="contact__item">
        <svg class="contact__icon" viewBox="0 0 20 20"><path d="M5 1.5l3 3.5-1.8 2.3c1 2.3 2.6 4 4.8 5.2l2.2-1.8 3.6 3-1.9 3c-6.5-.8-11.6-6-12.4-12.5z"/></svg>
        <span>(555) 240 1837</span>
      </li>
      <li class="contact__item">
        <svg class="contact__icon" viewBox="0 0 20 20"><path d="M10 1a9 9 0 1 0 4.5 16.8l-.9-1.6A7.2 7.2 0 1 1 17.2 10v1.1c0 1-.6 1.6-1.3 1.6s-1.2-.6-1.2-1.5V5.6h-1.8v.9A4.5 4.5 0 1 0 13.5 13c.6 1 1.5 1.5 2.5 1.5 1.9 0 3-1.5 3-3.4V10A9 9 0 0 0 10 1zm0 11.6a2.7 2.7 0 1 1 0-5.3 2.7 2.7 0 0 1 0 5.3z"/></svg>
        <span>hello@verdantrealty.com</span>
      </li>
      <li class="contact__item">
        <svg class="contact__icon" viewBox="0 0 20 20"><path d="M10 2l9 8h-3v8h-4.5v-5h-3v5H4v-8H1z"/></svg>
        <span>4180 Meadow Crest Way, Suite 210<br>Lakeview Hills, CA 92000</span>
      </li>
    </ul>

    <div class="person">
      <p class="person__name">Verdant Realty</p>
      <p class="person__title">Director</p>
    </div>

    <svg class="card__waves" viewBox="0 0 754 450" aria-hidden="true">
      <path d="M0 377 C 200 418, 520 420, 754 393 L754 450 L0 450 Z" fill="var(--slate)"/>
      <path d="M195 397 C 420 405, 620 392, 754 357 L754 373 C 610 400, 420 409, 195 397 Z" fill="var(--lime)"/>
    </svg>
  </section>

  <section class="card card--back">
    <div class="brand">
      <span class="brand__square"></span>
      <span class="brand__name">Verdant Realty</span>
    </div>
  </section>
</body>
</html>
```